Large corporation needs landing page for its employees with emotional and psychological problems

Vision:
Hello, we are a startup and would like to build a landing page and website in the mental health sector for a large corporation. In this site employees with emotional and psychological problems should quickly receive professional psychological support. This support takes the form of internal referrals from employees who are looking for help to qualified therapists, so that help can be provided quickly.
Furthermore, the employees get access to a tool where they can find out about topics in the mind health area and can also get help via webinars and podcasts. The employee should thus be able to take the hurdle to seek help and support in good time.
Therapists for whom the focus is on the urgency of providing quick help and support will work here in cooperation with the respective corporations.
Keywords:
• Help/Support
• overcome inhibitions
• Competent help
• Uncomplicated help
• Permanent access
• protected space
• Recognizing and naming emotional problems and actively tackling them
• get help
• mindfulness
• everyday helper
• Informative
• Anonymous
• compassion
• tolerance
• respect
• Appreciation
• empathy
• mindfulness
• protected space
• To be needed
• Like a lighthouse signal
What we need:
Landingpage
We need a landing page aimed at getting employees to contact psychological help. The call to action is to get in contact via a contact form.
Landing page content
There are several text modules:
• A heading/greeting
• A body of text at the beginning that explains the purpose of the page
• A bulleted text area describing the pain points and the solutions to them
Video:
The heart of the content will be a video explaining the need and inviting them to get in touch.
contact form:
It should be kept simple: first name, last name and email address
Legally required content:
General terms and conditions, data protection and imprint. These are only given as links in the footer.
In parallel, the Corporate Design should be adapted/extended:
Logo:
The font in the logo should be revised. The wings in the background remain.
Please adapt the logo for different uses:
• on a black background
• with transparent background
• favorite icon (browser)
• In square format for social media
Colors:
• develop a color chart based on the colors of the logo.
• please determine 2-3 main colors and the matching variations. I.e. transparent variations or light colors.
Typography:
Determine a decorative font and/or typography for headings and a text font. There should be no more than 3 fonts.
Updates
Need extra days to review
Industry/Entity Type
to recruit therapists as employees
Should not have
- please not to playful design or typography - and max. 3 colors

```html
<!DOCTYPE html>
<html lang="en">
<head>
<meta charset="utf-8">
<title>stillharbor — support for every employee</title>
<link href="https://fonts.googleapis.com/css2?family=Fira+Sans:wght@500;600&family=Inter:wght@400;500;600&display=swap" rel="stylesheet">
<style>
:root{
  --teal:#0b5563;
  --teal-deep:#093f4a;
  --teal-accent:#1e97a3;
  --orange:#f0a20c;
  --sky:#dcebef;
  --sky-soft:#eef5f7;
  --ink:#17262b;
  --muted:#5c6a6e;
  --line:#d9c9a8;
  --white:#ffffff;
}
*{box-sizing:border-box;margin:0;padding:0}
html,body{width:1200px;height:4996px;overflow:hidden}
body{position:relative;background:var(--white);font-family:"Inter",sans-serif;color:var(--ink)}
.abs{position:absolute}
h1,h2,h3,h4{font-family:"Fira Sans",sans-serif;font-weight:600}
a{color:inherit;text-decoration:none}
.btn{position:absolute;background:var(--orange);color:var(--white);font-size:12px;border-radius:4px;display:flex;align-items:center;justify-content:center}
.tag{position:absolute;font-size:9px;padding:3px 10px;border-radius:9px;background:#6fa7b0;color:#d7eef1}
.tag.light{background:#cfe6e3;color:#3b6b6e}
.photo{position:absolute;border-radius:8px}
.brand{font-family:"Fira Sans",sans-serif;font-weight:600;font-size:24px;color:var(--teal)}
.arrow-btn{position:absolute;width:26px;height:26px;border-radius:5px;display:flex;align-items:center;justify-content:center}

/* header */
.hero-panel{left:824px;top:0;width:376px;height:442px;background:var(--sky)}
.nav{left:420px;top:38px;display:flex;gap:34px;font-size:12px;color:#3b4a4e}
.nav .active{color:var(--teal-accent)}
.hero-title{left:110px;top:172px;font-size:37px;line-height:50px;color:var(--ink);width:420px}
.hero-title span{color:var(--teal-accent)}
.hero-text{left:110px;top:343px;width:400px;font-size:11.5px;line-height:16px;color:var(--muted)}
.watch{left:276px;top:405px;display:flex;align-items:center;gap:12px;font-size:12px;text-decoration:underline}

/* what we do */
.band{left:0;width:1200px;background:var(--teal)}
.wwd-title{left:54px;top:712px;font-size:29px;line-height:42px;color:var(--white);width:500px}
.wwd-text{left:54px;top:815px;width:780px;font-size:11.5px;line-height:16px;color:var(--white)}
.topics{left:32px;top:888px;display:flex}
.topic{width:250px;height:160px;padding:26px 22px;color:#a9c7cc}
.topic h3{font-size:17px;color:#d5e6e8;margin-bottom:16px}
.topic p{font-size:11.5px;line-height:16px}
.topic.on{background:var(--teal-deep);color:var(--white)}
.topic.on h3{color:var(--white)}

/* team */
.sec-title{left:54px;font-size:29px;color:var(--ink)}
.sec-rule{left:54px;width:1092px;height:2px;background:var(--line)}
.sec-link{font-size:11.5px;color:var(--muted);display:flex;gap:10px;align-items:center}
.member{position:absolute;top:1929px;width:240px;height:278px;border-radius:6px;overflow:hidden}
.member .shade{position:absolute;inset:0;background:linear-gradient(180deg,rgba(9,63,74,0) 40%,rgba(9,52,62,.95) 100%)}
.member h4{position:absolute;left:16px;top:212px;font-size:17px;color:var(--white)}
.member a{position:absolute;left:16px;top:243px;font-size:11px;color:var(--white);text-decoration:underline}

/* second band */
.b2-left{left:78px;top:2482px;width:350px;color:var(--white)}
.b2-left h2{font-size:31px;line-height:42px;margin:18px 0 22px}
.b2-left p{font-size:11.5px;line-height:16px;width:335px}
.b2-left .btn{position:static;width:120px;height:34px;margin-top:32px}
.b2-right-title{left:508px;top:2338px;font-size:29px;line-height:42px;color:var(--white);width:500px}
.b2-right-text{left:508px;top:2440px;width:610px;font-size:11.5px;line-height:16px;color:var(--white)}
.b2-card{position:absolute;top:2548px;width:239px;height:280px;background:var(--teal-deep);border-radius:6px;padding:22px 16px;color:var(--white);font-family:"Fira Sans",sans-serif;font-weight:600;font-size:17px;line-height:25px}

/* resources */
.res-meta{font-size:11px;color:var(--teal-accent)}
.res h3{font-size:20px;line-height:30px;color:var(--ink)}
.res-link{font-size:11px;text-decoration:underline;color:var(--ink)}

/* contact */
.contact-head{left:0;width:1200px;text-align:center;color:var(--white)}
.info{position:absolute;top:4105px;height:97px;display:flex;flex-direction:column;align-items:center;justify-content:center;gap:14px;font-size:13px;color:var(--white);font-weight:500}
.form-card{left:240px;top:4219px;width:720px;height:493px;background:var(--sky-soft);border-radius:10px}
.label{position:absolute;font-size:11.5px;color:var(--ink)}
.field{position:absolute;background:var(--sky);border-radius:4px;display:flex;align-items:center;padding-left:18px;gap:14px;font-size:13px}
.field.focus{background:var(--sky-soft);border:2px solid var(--teal)}

/* footer */
.footer{left:0;top:4851px;width:1200px;height:145px;background:var(--teal)}
</style>
</head>
<body>

<!-- header -->
<div class="abs hero-panel"></div>
<div class="abs brand" style="left:54px;top:32px">stillharbor</div>
<nav class="abs nav"><a class="active">Home</a><a>Articles</a><a>Diagnostic</a><a>About</a><a>Contact</a></nav>
<a class="btn" style="left:1016px;top:28px;width:128px;height:34px">Get In Touch</a>
<h1 class="abs hero-title">Don’t let your <span>struggle</span> become your identity, We got your back</h1>
<p class="abs hero-text">Lorem ipsum dolor sit amet, consectetur adipiscing elit. Donec cursus ligula non magna lobortis, vitae pretium quam pharetra.</p>
<a class="btn" style="left:110px;top:404px;width:128px;height:34px">Get In Touch</a>
<div class="abs watch"><span>Watch Video</span>
  <svg width="26" height="26" viewBox="0 0 26 26"><circle cx="13" cy="13" r="11.5" fill="none" stroke="#17262b" stroke-width="1.5"/><path d="M10 8l8 5-8 5z" fill="#17262b"/></svg>
</div>

<!-- what we do -->
<div class="abs band" style="top:510px;height:770px"></div>
<div class="photo" role="img" aria-label="Therapist listening to a client seated on a sofa in a bright room" style="left:535px;top:105px;width:625px;height:502px;background:linear-gradient(135deg,#e8e4df,#c9bfb4 55%,#d9d3cc)"></div>
<span class="tag" style="left:54px;top:688px">What We Do</span>
<h2 class="abs wwd-title">It’s your battle, but you don’t need to fight alone, we can help you</h2>
<a class="btn" style="left:1024px;top:720px;width:120px;height:34px">Learn More</a>
<p class="abs wwd-text">Lorem ipsum dolor sit amet, consectetur adipiscing elit. Donec cursus ligula non magna lobortis, vitae pretium quam pharetra. Morbi volutpat ipsum ut placerat tincidunt. Cras consectetur lorem ex, sit amet tincidunt purus rhoncus id.</p>
<div class="abs topics">
  <div class="topic"><h3>Anxiety</h3><p>Lorem ipsum dolor sit amet, consectetur adipiscing elit. Donec cursus ligula non magna lobortis, vitae pretium quam pharetra.</p></div>
  <div class="topic on"><h3>Phobia</h3><p>Lorem ipsum dolor sit amet, consectetur adipiscing elit. Donec cursus ligula non magna lobortis, vitae pretium quam pharetra.</p></div>
  <div class="topic"><h3>Addiction</h3><p>Lorem ipsum dolor sit amet, consectetur adipiscing elit. Donec cursus ligula non magna lobortis, vitae pretium quam pharetra.</p></div>
  <div class="topic"><h3>Despression</h3><p>Lorem ipsum dolor sit amet, consectetur adipiscing elit. Donec cursus ligula non magna lobortis, vitae pretium quam pharetra.</p></div>
  <div class="topic"><h3>Anger</h3><p>Lorem ipsum dolor sit amet, consectetur adipiscing elit. Donec cursus ligula non magna lobortis, vitae pretium quam pharetra.</p></div>
</div>
<div class="arrow-btn" style="left:922px;top:1085px;background:#3f6a4e"><svg width="12" height="12" viewBox="0 0 12 12"><path d="M10 6H2M5 3L2 6l3 3" stroke="#7f9a58" stroke-width="1.6" fill="none"/></svg></div>
<div class="abs" style="left:962px;top:1097px;width:140px;height:2px;background:var(--orange)"></div>
<div class="arrow-btn" style="left:1117px;top:1085px;background:#b8941c"><svg width="12" height="12" viewBox="0 0 12 12"><path d="M2 6h8M7 3l3 3-3 3" stroke="#2d3a20" stroke-width="1.6" fill="none"/></svg></div>

<!-- video -->
<div class="photo" role="img" aria-label="Video: therapist in conversation with a client in an office with bookshelves" style="left:169px;top:1179px;width:863px;height:512px;border-radius:10px;background:linear-gradient(120deg,#e9e7e3,#b7aea6 45%,#8b5a3f 80%,#c98a5d)"></div>
<svg class="abs" style="left:535px;top:1384px" width="102" height="102" viewBox="0 0 102 102" aria-label="Play video"><circle cx="51" cy="51" r="51" fill="#fff"/><path d="M40 30l32 21-32 21z" fill="#111"/></svg>

<!-- team -->
<span class="tag light" style="left:54px;top:1806px">Meet Our Team</span>
<h2 class="abs sec-title" style="top:1831px">More experts on our team</h2>
<a class="abs sec-link" style="left:1043px;top:1842px">meet all of us <svg width="12" height="10" viewBox="0 0 12 10"><path d="M1 5h9M7 2l3 3-3 3" stroke="#f0a20c" stroke-width="1.5" fill="none"/></svg></a>
<div class="abs sec-rule" style="top:1876px"></div>
<div class="member" style="left:78px" role="img" aria-label="Portrait of team therapist Mira Castell"><div class="abs" style="inset:0;background:linear-gradient(160deg,#e6e4e2,#b9b2ac)"></div><div class="shade"></div><h4>Mira Castell</h4><a>read more ↗</a></div>
<div class="member" style="left:345px" role="img" aria-label="Portrait of team therapist Owen Prescott"><div class="abs" style="inset:0;background:linear-gradient(160deg,#3f6b3a,#a9b6b8)"></div><div class="shade"></div><h4>Owen Prescott</h4><a>read more ↗</a></div>
<div class="member" style="left:613px" role="img" aria-label="Portrait of team therapist Nadia Vorel"><div class="abs" style="inset:0;background:linear-gradient(160deg,#d79a3d,#3c3c44)"></div><div class="shade"></div><h4>Nadia Vorel</h4><a>read more ↗</a></div>
<div class="member" style="left:882px" role="img" aria-label="Portrait of team therapist Julian Marsh"><div class="abs" style="inset:0;background:linear-gradient(160deg,#d9cfbf,#b49a6c)"></div><div class="shade"></div><h4>Julian Marsh</h4><a>read more ↗</a></div>

<!-- second band -->
<div class="abs band" style="top:2272px;height:704px"></div>
<div class="abs b2-left">
  <span class="tag" style="position:static;display:inline-block">What We Do</span>
  <h2>It’s your battle, but you don’t need to fight alone.</h2>
  <p>Lorem ipsum dolor sit amet, consectetur adipiscing elit. Donec cursus ligula non magna lobortis, vitae pretium quam pharetra. Morbi volutpat ipsum ut placerat tincidunt. Cras consectetur lorem ex, sit amet tincidunt purus rhoncus id.</p>
  <a class="btn">Learn More</a>
</div>
<h2 class="abs b2-right-title">It’s your battle, but you don’t need to fight alone.</h2>
<p class="abs b2-right-text">Lorem ipsum dolor sit amet, consectetur adipiscing elit. Donec cursus ligula non magna lobortis, vitae pretium quam pharetra. Morbi volutpat ipsum ut placerat tincidunt. Cras consectetur lorem ex, sit amet tincidunt purus rhoncus id.</p>
<div class="b2-card" style="left:508px">Lorem ipsum dolor.</div>
<div class="b2-card" style="left:772px">Lorem ipsum dolor sit amet, consectetur.</div>
<div class="b2-card" style="left:1035px;width:200px;white-space:nowrap">Lorem ipsum dolor<br>consectetur.</div>
<div class="arrow-btn" style="left:508px;top:2884px;background:#3f6a4e"><svg width="12" height="12" viewBox="0 0 12 12"><path d="M10 6H2M5 3L2 6l3 3" stroke="#7f9a58" stroke-width="1.6" fill="none"/></svg></div>
<div class="abs" style="left:549px;top:2896px;width:140px;height:2px;background:var(--orange)"></div>
<div class="arrow-btn" style="left:703px;top:2884px;background:#b8941c"><svg width="12" height="12" viewBox="0 0 12 12"><path d="M2 6h8M7 3l3 3-3 3" stroke="#2d3a20" stroke-width="1.6" fill="none"/></svg></div>

<!-- resources -->
<span class="tag light" style="left:54px;top:3090px">Contact Us</span>
<h2 class="abs sec-title" style="top:3116px">Learn from our experts</h2>
<a class="abs sec-link" style="left:1008px;top:3127px">View All Resources <svg width="12" height="10" viewBox="0 0 12 10"><path d="M1 5h9M7 2l3 3-3 3" stroke="#f0a20c" stroke-width="1.5" fill="none"/></svg></a>
<div class="abs sec-rule" style="top:3161px"></div>
<div class="photo" role="img" aria-label="Group therapy session in a bright room with yellow chairs" style="left:54px;top:3191px;width:520px;height:398px;background:linear-gradient(135deg,#eeeae4,#c9b89d 50%,#a8a39b)"></div>
<div class="abs res" style="left:54px;top:3610px;width:520px">
  <div class="res-meta">Article</div>
  <h3 style="font-size:20px;margin:6px 0 10px">Self Punish Often? How to Course Correct without Chastising</h3>
  <p style="font-size:11.5px;line-height:16px;color:var(--muted);margin-bottom:16px">Lorem ipsum dolor sit amet, consectetur adipiscing elit. Sed id felis pretium, dapibus nulla id, pharetra lacus. Donec fringilla mauris ut vulputate dignissim.</p>
  <a class="res-link">read more <span style="color:var(--orange)">↗</span></a>
</div>
<div class="photo" role="img" aria-label="Laptop showing a video call next to a green mug" style="left:611px;top:3191px;width:279px;height:179px;background:linear-gradient(135deg,#8a5a30,#3d4a4c 55%,#b7a48a)"></div>
<div class="abs res" style="left:911px;top:3208px;width:240px">
  <div class="res-meta">Podcast</div>
  <h3 style="margin:4px 0 10px">What Is the Grey Rock Method and Is It Effective?</h3>
  <a class="res-link">Listen now <span style="color:var(--orange)">↗</span></a>
</div>
<div class="photo" role="img" aria-label="Video: people talking around a kitchen table" style="left:611px;top:3395px;width:279px;height:178px;background:linear-gradient(135deg,#c9c2b4,#5a4a3a 55%,#a88a63)"></div>
<svg class="abs" style="left:731px;top:3465px" width="38" height="38" viewBox="0 0 38 38" aria-label="Play video"><circle cx="19" cy="19" r="19" fill="#fff"/><path d="M15 11l12 8-12 8z" fill="#111"/></svg>
<div class="abs res" style="left:911px;top:3412px;width:240px">
  <div class="res-meta">Video</div>
  <h3 style="margin:4px 0 10px">Does Success Lead to Happiness?</h3>
  <a class="res-link">Watch more <span style="color:var(--orange)">↗</span></a>
</div>
<div class="photo" role="img" aria-label="Two people in a warm supportive conversation" style="left:611px;top:3599px;width:279px;height:178px;background:linear-gradient(135deg,#e2ded8,#9b8f82 50%,#c8a43a)"></div>
<div class="abs res" style="left:911px;top:3616px;width:240px">
  <div class="res-meta">Article</div>
  <h3 style="margin:4px 0 10px">Can Depression Affect Your Empathy Levels?</h3>
  <a class="res-link">read more <span style="color:var(--orange)">↗</span></a>
</div>

<!-- contact -->
<div class="abs band" style="top:3874px;height:500px"></div>
<div class="abs contact-head" style="top:3942px"><span class="tag" style="position:static;display:inline-block">Get In Touch</span></div>
<h2 class="abs contact-head" style="top:3972px;font-size:29px">Get in touch, we're here for you</h2>
<p class="abs" style="left:290px;top:4026px;width:620px;text-align:center;font-size:11.5px;line-height:16px;color:var(--white)">Lorem ipsum dolor sit amet, consectetur adipiscing elit. Donec cursus ligula non magna lobortis, vitae pretium quam pharetra.</p>
<div class="info" style="left:320px;width:190px">
  <svg width="14" height="16" viewBox="0 0 14 16"><path d="M7 1a5 5 0 0 0-5 5c0 4 5 9 5 9s5-5 5-9a5 5 0 0 0-5-5z" fill="#1e97a3"/><circle cx="7" cy="6" r="1.8" fill="#0b5563"/></svg>
  <span>118 Linden Row, Ashford</span>
</div>
<div class="info" style="left:530px;width:140px">
  <svg width="16" height="16" viewBox="0 0 16 16"><path d="M3 1l3 1 1 4-2 1c1 2 2 3 4 4l1-2 4 1 1 3c-1 2-3 2-5 1C6 12 4 10 2 6 1 4 1 2 3 1z" fill="#1e97a3"/></svg>
  <span>555-014-2287</span>
</div>
<div class="info" style="left:692px;width:183px;background:var(--teal-deep)">
  <svg width="16" height="12" viewBox="0 0 16 12"><rect width="16" height="12" rx="1.5" fill="#1e97a3"/><path d="M1 1l7 5 7-5" stroke="#093f4a" stroke-width="1.4" fill="none"/></svg>
  <span>hello@stillharbor.org</span>
</div>
<div class="abs form-card"></div>
<span class="label" style="left:285px;top:4266px">Your Name</span>
<div class="field" style="left:285px;top:4291px;width:293px;height:54px">
  <svg width="16" height="16" viewBox="0 0 16 16"><circle cx="8" cy="8" r="7" fill="none" stroke="#0b5563" stroke-width="1.4"/><circle cx="8" cy="6.5" r="2.3" fill="#0b5563"/><path d="M3.5 13c1-2.5 8-2.5 9 0" fill="#0b5563"/></svg>
  <span>Tessa Quill</span>
</div>
<span class="label" style="left:285px;top:4380px">Email</span>
<div class="field focus" style="left:285px;top:4405px;width:293px;height:57px">
  <svg width="16" height="12" viewBox="0 0 16 12"><rect width="16" height="12" rx="1.5" fill="#0b5563"/><path d="M1 1l7 5 7-5" stroke="#eef5f7" stroke-width="1.4" fill="none"/></svg>
</div>
<span class="label" style="left:285px;top:4495px">Phone</span>
<div class="field" style="left:285px;top:4520px;width:293px;height:56px">
  <svg width="12" height="18" viewBox="0 0 12 18"><rect x="1" y="1" width="10" height="16" rx="2" fill="none" stroke="#0b5563" stroke-width="1.6"/><rect x="4" y="13.5" width="4" height="1.4" fill="#0b5563"/></svg>
</div>
<span class="label" style="left:622px;top:4266px">Message</span>
<div class="field" style="left:622px;top:4291px;width:293px;height:242px"></div>
<a class="btn" style="left:529px;top:4634px;width:140px;height:35px">Send Message</a>

<!-- footer -->
<footer class="abs footer">
  <div class="abs" style="left:54px;top:56px;display:flex;align-items:center;gap:10px">
    <span style="width:12px;height:12px;border-radius:50%;background:var(--orange)"></span>
    <span class="brand" style="color:var(--white)">stillharbor</span>
  </div>
  <div class="abs" style="left:240px;top:74px;width:906px;height:1px;background:#4f8893"></div>
  <div class="abs" style="left:820px;top:46px;width:326px;text-align:right;font-size:11.5px;color:var(--white)">Data protection and imprint &nbsp; • &nbsp; Terms and conditions</div>
  <div class="abs" style="left:820px;top:88px;width:326px;text-align:right;font-size:11.5px;color:var(--white)">Copyright © 2023 Stillharbor</div>
</footer>

</body>
</html>
```